Home Page Redesign for Pet Website

Looking to redesign the home page of our WORDPRESS website which will be renamed The Critter Cover Handbook 2015.

Looking for clean design which communicates clarity.
Updates

This is for a Wordpress site.

Please note that the design MUST include the content which is shown in the table in the brief!

Hi Thanks for the designs so far. We have just updated the brief to provide more information and clarify a few issues. We have also now included a couple of layout suggestions. They are just suggestions but it should give you a better idea of what we are looking for. And we have just increased the budget for 1st place by £120. Please feel free to message me if you have any questions. Many thanks. Maud

Please note that the new brief is in a file dated 25 Jan!

Reason: We have extended the deadline so we can continue working with the designers who have submitted designs we like. If you have any new designs please submit them by the original deadline of 7.37pm this evening (GMT). We are planning to make our final decision by Friday this week.

Target Market(s)

UK pet owners. All ages but largest age group is 35-50.

Industry/Entity Type

Insurance

Requirements
Must have
• Three clear content groups - LEARN, RESEARCH, CAMPAIGN (see brief for more details).
Stock photos with dogs and cats
Use current colour scheme
Must work with existing inner pages.
Existing font.. but 1pt larger
See brief for more details
Should not have
• Logo
Content from Existing Page (except for footer content... and menu headings).

```html
<!DOCTYPE html>
<html lang="en">
<head>
<meta charset="utf-8">
<title>The Critter Cover Handbook 2015</title>
<link href="https://fonts.googleapis.com/css2?family=Raleway:wght@400;500;600&family=Open+Sans:wght@400;600;700&display=swap" rel="stylesheet">
<style>
:root{
  --orange:#f47b20;
  --orange-dark:#e0661a;
  --title-orange:#f05a1a;
  --blue:#3a62c3;
  --hero-blue:#2c4aa6;
  --purple:#4f2a8c;
  --teal:#1ea58a;
  --text:#555;
  --muted:#888;
  --line:#d8d8d8;
  --footer:#efefef;
  --footer-base:#e4e4e4;
  --widget-head:#bcd3ea;
  --chirp:#45b4e0;
}
*{box-sizing:border-box;margin:0;padding:0}
html,body{width:766px;height:1200px;overflow:hidden;background:#fff}
body{position:relative;font-family:"Open Sans",Arial,sans-serif;color:var(--text);font-size:7px;line-height:1.5}
.abs{position:absolute}
h1,h2,h3,h4{font-family:"Raleway",Arial,sans-serif;font-weight:500}

.brand{left:101px;top:18px}
.brand-name{font-family:"Raleway",sans-serif;font-size:15px;line-height:15px;font-weight:500;color:var(--orange)}
.brand-name span{color:var(--blue);display:block}
.brand-tag{font-size:6.5px;color:#333;margin-top:3px}
.social-top{right:104px;top:27px;display:flex;gap:6px;font-size:7px;font-weight:600;color:var(--blue)}
.search{left:525px;top:45px;width:139px;height:18px;border:1px solid #ccc;font-size:6px;color:#777;padding:4px 7px}
.search svg{position:absolute;right:6px;top:4px}

.nav{left:0;top:70px;width:766px;height:27px;background:linear-gradient(var(--orange),var(--orange-dark));display:flex;padding-left:114px}
.nav a{color:#fff;text-decoration:none;font-family:"Raleway",sans-serif;font-size:8px;padding:0 10px;line-height:27px;border-right:1px solid rgba(255,255,255,.35)}
.nav a:last-child{border:none}

.hero{left:0;top:97px;width:766px;height:267px;background:linear-gradient(180deg,#1a1f12 0%,#3a4a22 40%,#6b7f3a 70%,#8da24a 100%)}
.hero-box{left:101px;top:186px;width:243px;height:104px;background:var(--hero-blue);padding:18px 19px;color:#fff}
.hero-box h1{font-size:18.5px;line-height:22px;font-weight:400;white-space:nowrap}
.hero-box h2{font-size:12px;color:#9fb8ff;font-weight:400;margin-top:2px;white-space:nowrap}
.hero-box p{font-size:6px;margin-top:6px;line-height:10px}

.card{top:374px;width:183px}
.card .photo{height:76px}
.card h3{font-size:11px;margin-top:9px;font-weight:400}
.card p{font-size:6px;color:var(--muted);line-height:9.5px;margin-top:3px}
.btn{display:inline-block;margin-top:7px;padding:3px 10px;color:#fff;font-size:5.5px;font-weight:700;border-radius:2px}

.groups{left:102px;top:554px;width:564px;height:232px;border:1px solid var(--line);display:flex}
.group{border-right:1px solid var(--line);position:relative}
.group:last-child{border:none}
.group-head{height:38px;border-bottom:1px solid var(--line);padding:8px 0 0 22px;background:linear-gradient(#fff,#f7f7f7)}
.group-head small{display:block;font-family:"Raleway",sans-serif;font-size:9px;color:#333;line-height:10px}
.group-head h3{font-size:12px;color:var(--blue);line-height:14px}
.group-head h3.accent{color:var(--title-orange)}
.group ul{list-style:none;padding:7px 22px 0;font-size:6.5px;color:#444}
.group li{line-height:9px;margin-bottom:9px}
.providers{display:flex;gap:30px;padding:0 24px;font-size:6.5px;color:#444}
.providers div span{display:block;line-height:13.3px}

.section-title{left:104px;top:818px;font-size:14px;color:var(--blue);font-family:"Raleway",sans-serif}
.article{top:845px;display:flex;gap:6px;width:230px}
.article .photo{width:76px;height:67px;flex:none}
.article h4{font-size:8px;color:var(--purple);line-height:10px}
.article p{font-size:6px;line-height:10.5px;color:var(--muted)}
.article .more{font-size:6px;color:#333;margin-top:3px}
.promo{left:567px;top:834px;width:97px;height:96px;background:linear-gradient(160deg,#1a3a7a,#0f5fa8 60%,#2bb34a)}

.footer{left:0;top:954px;width:766px;height:206px;background:var(--footer)}
.footer-base{left:0;top:1160px;width:766px;height:40px;background:var(--footer-base);padding:18px 101px;font-size:6.5px;color:#444}
.widget{top:977px;width:132px;height:165px;background:#fff;border:1px solid #ddd;overflow:hidden}
.widget-head{height:18px;font-size:8px;color:#333;padding:3px 12px;font-family:"Raleway",sans-serif;font-weight:500}
.widget-body{padding:4px 6px;font-size:5.5px;line-height:8px;color:#333}
.avatar{width:18px;height:20px;background:#c9b8a8;float:left;margin-right:5px}
.post{border:1px solid #ddd;margin-top:8px;padding:5px;height:95px;overflow:hidden}
.link{color:var(--blue)}
.tweet-img{height:28px;background:linear-gradient(#3a6a2a,#7aa84a);margin-top:5px}
.foot-col{top:977px}
.foot-col h3{font-size:12px;color:var(--teal)}
.foot-col p,.foot-col li{font-size:6.5px;color:#555}
.chip{display:inline-block;font-size:5.5px;font-weight:700;color:#333;margin-top:4px}
.chip.blue{background:var(--blue);color:#fff;padding:1px 4px;border-radius:2px}
.foot-col ul{list-style:none;margin-top:14px}
.foot-col li{margin-bottom:6px}
.disclaimer p{font-size:6px;line-height:10.6px;color:var(--muted);width:130px;margin-top:4px}
</style>
</head>
<body>

<div class="abs brand">
  <div class="brand-name">The Critter Cover<span>Handbook 2015</span></div>
  <div class="brand-tag">Independent unbiased information for fellow pet owners.</div>
</div>
<div class="abs social-top"><span>Chirper</span><span>Friendsheet</span><span>Linkwork</span></div>
<div class="abs search">Search here
  <svg width="9" height="9" viewBox="0 0 10 10"><circle cx="4" cy="4" r="3" fill="none" stroke="#444" stroke-width="1.3"/><line x1="6.3" y1="6.3" x2="9.3" y2="9.3" stroke="#444" stroke-width="1.4"/></svg>
</div>

<nav class="abs nav">
  <a>Home</a><a>Pet Insurance Reviews</a><a>Providers A-Z</a><a>Pet Insurance Policies</a><a>Surveys</a><a>More</a>
</nav>

<div class="abs hero" role="img" aria-label="Photo of a puppy and a kitten on grass"></div>
<div class="abs hero-box">
  <h1>Critter Cover Handbook</h1>
  <h2>Curabitur iaculis tempus eros</h2>
  <p>Etiam est nunc venenatis in tristique eu imperdiet ac nisl Cum sociis natoque penatibus et magnis dis parturient</p>
</div>

<div class="abs card" style="left:101px">
  <div class="photo" role="img" aria-label="Photo of a dog running across a field" style="background:linear-gradient(#5a7a3a,#c98a3a 60%,#6a8a3a)"></div>
  <h3 style="color:var(--purple)">PET INSURANCE PROIVIDER</h3>
  <p>Mauris vel lacus vitae felis vestibulum volutpat Etiam est nunc venenatis in tristique eu imperdiet ac nisl Cum sociis natoque penatibus et magnis dis parturient montes</p>
  <span class="btn" style="background:var(--purple)">READ MORE</span>
</div>
<div class="abs card" style="left:294px">
  <div class="photo" role="img" aria-label="Photo of a dog resting with a cat" style="background:linear-gradient(120deg,#8a6a4a,#d8b88a 50%,#6a5a4a)"></div>
  <h3 style="color:var(--title-orange)">TOP POLICIES</h3>
  <p>Mauris vel lacus vitae felis vestibulum volutpat Etiam est nunc venenatis in tristique eu imperdiet ac nisl Cum sociis natoque penatibus et magnis dis parturient montes</p>
  <span class="btn" style="background:var(--title-orange)">READ MORE</span>
</div>
<div class="abs card" style="left:485px">
  <div class="photo" role="img" aria-label="Photo of a cat lying in grass" style="background:linear-gradient(120deg,#7ab84a,#c8c8c8 50%,#5a9a3a)"></div>
  <h3 style="color:var(--teal)">BIO</h3>
  <p>Mauris vel lacus vitae felis vestibulum volutpat Etiam est nunc venenatis in tristique eu imperdiet ac nisl Cum sociis natoque penatibus et magnis dis parturient montes</p>
  <span class="btn" style="background:var(--teal)">READ MORE</span>
</div>

<section class="abs groups">
  <div class="group" style="width:185px">
    <div class="group-head"><small>Learn</small><h3>About Pet Insurance</h3></div>
    <ul style="padding-left:23px">
      <li>Introduction to Pet Insurance</li><li>Vet Fees Cover Types</li><li>What to Consider before Buying</li>
      <li>Ten Popular Pet Insurance Providers</li><li>Confused by Pet Insurance: Start Here!</li><li>Third Party Liability Insurance</li>
      <li>Six Vet Fees Pet Insurance Companies Won't Pay!</li><li>Why Cheap Pet Insurance is Risky</li><li>Why Your Pets Vet History is Important</li>
    </ul>
  </div>
  <div class="group" style="width:190px">
    <div class="group-head"><small>Research</small><h3 class="accent">UK Pet Insurance</h3></div>
    <p style="font-size:6.5px;font-weight:600;color:#333;padding:7px 24px 3px">Analysis, Customer Reviews</p>
    <div class="providers">
      <div><span>Paw Partners</span><span>Brightcart</span><span>Straight Cover</span><span>K&amp;T</span><span>Happy Tails</span><span>Coverhelp</span><span>Hale &amp; Moss</span><span>QM=</span></div>
      <div style="padding-top:3px"><span>Whisker Club</span><span>R&amp;D Stores</span><span>Beyond Cover</span><span>Furplan</span><span>Greengrove's</span><span>Valuemart</span><span>Meridian Money</span></div>
    </div>
    <p style="font-size:6.5px;color:#444;padding:6px 24px 0 23px;line-height:10.5px">Search our database for policies matching your criteria</p>
    <p style="font-size:6.5px;color:#444;padding:7px 24px 0 23px;line-height:10.5px">Compare claims experiences for pet insurance providers</p>
  </div>
  <div class="group" style="width:187px">
    <div class="group-head"><small>Campaign</small><h3>For Fairer Pet Insurance</h3></div>
    <ul style="padding-top:13px">
      <li>This section will contain paragraphs of text</li><li>Brief explanation of why a campaign is needed.</li><li>Brief explanation of what to campaign for.</li>
      <li>Bio pic of me... plus brief bio.</li><li>How you can help</li><li>Stories with Pet Pics.</li>
    </ul>
  </div>
</section>

<h2 class="abs section-title">Popular Articles and Resources</h2>
<div class="abs article" style="left:105px">
  <div class="photo" role="img" aria-label="Photo of a small dog running on grass" style="background:linear-gradient(#9ac06a,#d8a060 55%,#6a9a3a)"></div>
  <div><h4>Pet Insurance for Pre-Existing Conditions</h4><p>Aascetur ridiculus mus In iaculis facilisis massa Etiam eu urna Sed porta Suspendisse quam leo molestie sed luctus quis feugiat in pede Fusce tellus Sed metus</p><div class="more">Read More</div></div>
</div>
<div class="abs article" style="left:338px">
  <div class="photo" role="img" aria-label="Photo of a sleeping dog" style="background:linear-gradient(135deg,#3a2a1a,#a07050 60%,#4a3020)"></div>
  <div><h4>Pet Insurance for Pre-Existing Conditions</h4><p>Aascetur ridiculus mus In iaculis facilisis massa Etiam eu urna Sed porta Suspendisse quam leo molestie sed luctus quis feugiat in pede Fusce tellus Sed metus</p><div class="more">Read More</div></div>
</div>
<div class="abs promo" role="img" aria-label="Advert for web hosting packages"></div>

<footer>
  <div class="abs footer"></div>

  <div class="abs widget" style="left:102px">
    <div class="widget-head" style="background:var(--widget-head)">Join Us on Friendsheet</div>
    <div class="widget-body">
      <div class="avatar"></div>
      <b class="link">Critter Cover Surveys UK</b><br><span class="chip blue">Like</span> 1,176
      <div class="post"><div class="avatar"></div><b class="link">Critter Cover Surveys UK</b><br><span style="color:#999">January 19 at 1:13pm</span><br><br>Pet Insurance Premium Increases<br><br>Interesting article from Compare Weekly suggesting that pet insurance premiums can double as your pet ages...<br><br>Have to confess that this sounds on the low side to me! Would be really</div>
    </div>
  </div>

  <div class="abs widget" style="left:253px">
    <div class="widget-head" style="background:var(--chirp);color:#fff">Latest from Chirper</div>
    <div class="widget-body">
      <b>Tweets</b> <span style="float:right" class="chip">Follow</span><br>
      <span class="link">pawfinder.example/dog-blog.php?d...</span>
      <div style="margin-top:14px"><div class="avatar" style="width:12px;height:13px"></div><b>Critter Cover Surveys</b> <span style="float:right">16 Jun</span><br>@CritterCoverUK</div>
      <div>RT <span class="link">@listeningpaws</span>: Not into football? We have 14 adorable hearing dog puppies who will change your mind <span class="link">#SummerKickabout</span> <span class="link">pic.chirper.example/k4Wm2xQ</span></div>
      <div class="tweet-img" role="img" aria-label="Photo of a puppy on grass"></div>
      <div style="border:1px solid #ccc;margin-top:6px;padding:2px 4px;color:#777">Tweet to @CritterCoverUK</div>
    </div>
  </div>

  <div class="abs foot-col" style="left:409px">
    <h3>Follow Us</h3>
    <span class="chip">Follow @CritterCoverUK</span><br>
    <span class="chip blue">Like</span><br>
    <span class="chip">Circles Follow</span>
    <ul><li>About Us</li><li>Legal Information &amp; Disclaimers</li><li>Privacy Policy</li></ul>
  </div>

  <div class="abs foot-col disclaimer" style="left:536px">
    <h3>Disclaimer</h3>
    <p>Please note that pet insurance terms often change. Whilst we will do our best to keep this website up to date you must check with the appropriate insurer before making any decisions. If you find any mistakes on this website please do let us know so we can correct it for the benefit of future visitors. Many thanks! - See more at:</p>
  </div>

  <div class="abs footer-base">Copyright © 2015. Critter Cover Surveys UK. All Right Reserved.</div>
</footer>

</body>
</html>
```